Moscato Wine Brand Graphic Design - see photos for reference and sizing guide

In need of a graphic design for our brand VELVET MUSE Pink Moscato with the following requirements:1. Lantawan Theme - it is a popular festival in Philippines that means "many faces" and is symbolized by creative masks with vibrant colours and designs.2. We want a Lantawan Design on our moscato bottle to represent women as Velvet Muses.3. The lantawan has to be bright,colourful, with pink,purple,musk,greys,small silver and gold stars or stripes glitter or sparkle accents to it.4. It has to have a WOW Factor, feel good label design that is aimed at Women 18yrs to 45yrs old.5. A sample is provided but feel free to play around and the most vibrant, new world design for VELVET MUSE Pink Moscato label Wins.

Target Market(s)

Women 18 to 45 yrs of age, Asian and Western Market

Font styles to use
Script

Colors

Designer to choose colors to be used in the design.

Requirements
Must have
• Bright,Bold and Vibrant Design that matches the label and it has to be a sophisticated Mask Design please refer to photo as a guide. Let your imagination run wild.
• Label Measurements: Front Label
• Width: 125mm
• Height:95mm
• Height from Base: 21mm
Nice to have
• Accents of sparkles and glitter with gold,silver,purple,pink hues or use your creativity to create a stunning mask design. The wine bottle is in Arctic Blue Sparkling Wine Bottle that makes the bottle look like light purple once the wine is in it so put it in consideration when making the label and background.

```html
<!DOCTYPE html>
<html lang="en">
<head>
<meta charset="utf-8">
<title>Velvet Muse Pink Moscato – Front Label</title>
<link rel="stylesheet" href="https://fonts.googleapis.com/css2?family=Great+Vibes&family=Poiret+One&family=Josefin+Sans:wght@300&display=swap">
<style>
  :root {
    --backdrop: #0d0b10;
    --label-silver-light: #e4dcef;
    --label-silver-mid: #b9b2c4;
    --label-silver-dark: #9f99a8;
    --ink: #2a2530;
    --brand-pink: #c8519e;
    --mask-pink: #e468b4;
    --mask-lilac: #c8b5e0;
    --mask-gold: #f2c94c;
    --dot-grey: #55505c;
  }
  html, body {
    margin: 0;
    padding: 0;
    width: 1200px;
    height: 2467px;
    overflow: hidden;
    background: var(--backdrop);
  }
  .canvas {
    position: relative;
    width: 1200px;
    height: 2467px;
  }
  .front-label {
    position: absolute;
    left: 100px;
    top: 418px;
    width: 1000px;
    height: 1630px;
    background: linear-gradient(90deg,
      var(--label-silver-dark) 0%,
      var(--label-silver-light) 22%,
      var(--label-silver-mid) 40%,
      var(--label-silver-light) 58%,
      var(--label-silver-mid) 78%,
      var(--label-silver-light) 100%);
  }
  .mask-artwork {
    position: absolute;
    left: 85px;
    top: 85px;
    width: 830px;
    height: 830px;
    display: block;
  }
  .brand-name {
    position: absolute;
    left: 0;
    top: 1010px;
    width: 100%;
    margin: 0;
    text-align: center;
    font-family: "Great Vibes", cursive;
    font-weight: 400;
    font-size: 190px;
    line-height: 1;
    color: var(--brand-pink);
  }
  .varietal {
    position: absolute;
    left: 35px;
    right: 35px;
    top: 1232px;
    display: flex;
    align-items: center;
    gap: 28px;
  }
  .varietal-rule {
    flex: 1;
    border-top: 5px dotted var(--dot-grey);
  }
  .varietal-name {
    margin: 0;
    font-family: "Poiret One", sans-serif;
    font-size: 92px;
    letter-spacing: 8px;
    color: var(--ink);
    line-height: 1;
  }
  .bottle-facts {
    position: absolute;
    left: 0;
    top: 1432px;
    width: 100%;
    text-align: center;
    font-family: "Josefin Sans", sans-serif;
    font-weight: 300;
    font-size: 42px;
    letter-spacing: 3px;
    line-height: 58px;
    color: var(--ink);
  }
  .bottle-facts p { margin: 0; }
</style>
</head>
<body>
<main class="canvas">
  <section class="front-label">
    <svg class="mask-artwork" viewBox="0 0 830 830" role="img" aria-label="Ornate festival mask illustration with pink, lilac, silver and gold petal plumes">
      <defs>
        <radialGradient id="maskGlow" cx="50%" cy="55%" r="55%">
          <stop offset="0%" stop-color="var(--mask-gold)" stop-opacity="0.55"/>
          <stop offset="40%" stop-color="var(--mask-pink)" stop-opacity="0.45"/>
          <stop offset="75%" stop-color="var(--mask-lilac)" stop-opacity="0.35"/>
          <stop offset="100%" stop-color="var(--mask-lilac)" stop-opacity="0"/>
        </radialGradient>
      </defs>
      <rect width="830" height="830" fill="url(#maskGlow)"/>
    </svg>

    <h1 class="brand-name">Velvet Muse</h1>

    <div class="varietal">
      <span class="varietal-rule"></span>
      <h2 class="varietal-name">PINK MOSCATO</h2>
      <span class="varietal-rule"></span>
    </div>

    <div class="bottle-facts">
      <p>0.75L</p>
      <p>13% ALC.</p>
    </div>
  </section>
</main>
</body>
</html>
```